Hack my website! Tall Harbor needs a site

We hack stuff. No joke, that is what we do, but we are the good guys!

We do security consulting, specifically offensive security. The technical term is "Penetration Testing", but you probably know it as "hacking". Companies hire us to break in before the bad guys do. (I have a very cool job :) ).

I need a web site to describe our offerings and connect with clients.

I've included my business card and logo so you can understand what I'm looking for on the website and the color scheme.

Tag line:
Offensive Services from Offensive Minds

Target Market(s)

Medium to large businesses

Industry/Entity Type

Computer Security

Coding

Coded - Design and coding required

Number of Pages Required

2 page

Font styles to use
Sans Serif

Colors

Designer to choose colors to be used in the design.

Requirements
Must have
• Flat, clean, professional look
Nice to have
• Bonus for bootstrap. See the uploaded logo for the current colors. I'd really like this to look decent on a phone too.
Should not have
• 1. Black background
• 2. The business card is to show the colors and theme so far. Please, do NOT just slam that into the middle of the site since it doesn't make sense. It feels odd that I have to say that, but I've received multiple submissions where people have done this.

```html
<!DOCTYPE html>
<html lang="en">
<head>
<meta charset="utf-8">
<title>Tall Harbor – Services</title>
<link rel="stylesheet" href="https://fonts.googleapis.com/css2?family=Noto+Sans:wght@400;500&display=swap">
<style>
  :root {
    --header-bg: #7f7f7f;
    --footer-bg: #646464;
    --brand-red: #d8262e;
    --brand-dark: #3a3a3a;
    --ink: #000000;
    --page: #ffffff;
    --hero-left-a: #16191c;
    --hero-left-b: #2d3134;
    --hero-right-a: #2a2c2f;
    --hero-right-b: #6b6e72;
  }
  * { box-sizing: border-box; margin: 0; padding: 0; }
  html, body { width: 1170px; height: 1200px; overflow: hidden; }
  body {
    position: relative;
    background: var(--page);
    color: var(--ink);
    font-family: "Noto Sans", sans-serif;
  }
  .site-header {
    position: absolute; left: 0; top: 0; width: 1170px; height: 101px;
    background: var(--header-bg);
    border-bottom: 1px solid #6a6a6a;
  }
  .brand {
    position: absolute; left: 31px; top: 26px;
    display: flex; align-items: center; gap: 20px;
  }
  .brand-mark { width: 46px; height: 46px; background: var(--brand-red); }
  .brand-name {
    font-size: 40px; font-weight: 400; letter-spacing: 9px;
    color: var(--brand-red); line-height: 1;
  }
  .main-nav { position: absolute; top: 27px; right: 0; display: flex; }
  .main-nav a {
    color: var(--ink); text-decoration: none; font-size: 36px; line-height: 1.2;
  }
  .main-nav .nav-home { position: absolute; left: -372px; }
  .main-nav .nav-services { position: absolute; left: -204px; }

  .hero { position: absolute; left: 0; top: 101px; width: 1170px; height: 339px; display: flex; }
  .hero-photo-security {
    width: 640px; height: 100%;
    background: linear-gradient(160deg, var(--hero-left-b), var(--hero-left-a) 70%);
  }
  .hero-photo-servers {
    flex: 1; height: 100%; border-left: 1px solid #555;
    background: linear-gradient(120deg, var(--hero-right-a), var(--hero-right-b));
  }

  .services-title {
    position: absolute; top: 492px; width: 100%;
    text-align: center; font-size: 52px; font-weight: 400; line-height: 1.2;
  }
  .divider { position: absolute; top: 576px; left: 0; width: 1170px; height: 50px; }
  .divider-line { position: absolute; top: 23px; height: 4px; width: 146px; background: var(--ink); }
  .divider-line.left { left: 219px; }
  .divider-line.right { left: 805px; }
  .divider-icon { position: absolute; top: 3px; width: 46px; height: 46px; }

  .service-list {
    position: absolute; top: 655px; width: 100%;
    list-style: none; text-align: center; font-size: 23px; line-height: 46.3px;
  }

  .site-footer {
    position: absolute; left: 0; top: 1006px; width: 1170px; height: 194px;
    background: var(--footer-bg); border-top: 1px solid #555;
  }
  .contact-title { position: absolute; left: 52px; top: 22px; font-size: 29px; font-weight: 400; }
  .contact-list { position: absolute; left: 52px; top: 66px; list-style: none; font-size: 19px; line-height: 25px; }
  .contact-list li { display: flex; align-items: center; gap: 5px; }
  .contact-list svg { width: 17px; height: 17px; }
  .copyright { position: absolute; right: 20px; top: 147px; font-size: 19px; }
</style>
</head>
<body>
  <header class="site-header">
    <div class="brand">
      <span class="brand-mark"></span>
      <span class="brand-name">TALL HARBOR</span>
    </div>
    <nav class="main-nav">
      <a class="nav-home" href="#">Home</a>
      <a class="nav-services" href="#">Services</a>
    </nav>
  </header>

  <section class="hero">
    <div class="hero-photo-security" role="img" aria-label="Photo of a screen showing the word Security with a pointing cursor"></div>
    <div class="hero-photo-servers" role="img" aria-label="Photo of rack-mounted servers with status lights"></div>
  </section>

  <h1 class="services-title">Our Services</h1>

  <div class="divider">
    <span class="divider-line left"></span>
    <svg class="divider-icon" style="left:413px" viewBox="0 0 46 46" aria-hidden="true">
      <circle cx="19" cy="19" r="12" fill="none" stroke="#000" stroke-width="6"/>
      <line x1="28" y1="28" x2="40" y2="40" stroke="#000" stroke-width="8" stroke-linecap="round"/>
    </svg>
    <svg class="divider-icon" style="left:510px" viewBox="0 0 46 46" aria-hidden="true">
      <path d="M14 21v-6a9 9 0 0 1 18 0v6" fill="none" stroke="#000" stroke-width="5"/>
      <rect x="9" y="20" width="28" height="22" rx="3" fill="#000"/>
    </svg>
    <svg class="divider-icon" style="left:608px" viewBox="0 0 46 46" aria-hidden="true">
      <g fill="#000">
        <circle cx="17" cy="27" r="11"/>
        <g stroke="#000" stroke-width="5">
          <line x1="17" y1="12" x2="17" y2="42"/><line x1="2" y1="27" x2="32" y2="27"/>
          <line x1="6" y1="16" x2="28" y2="38"/><line x1="28" y1="16" x2="6" y2="38"/>
        </g>
        <circle cx="35" cy="11" r="6"/>
        <g stroke="#000" stroke-width="3">
          <line x1="35" y1="2" x2="35" y2="20"/><line x1="26" y1="11" x2="44" y2="11"/>
        </g>
      </g>
      <circle cx="17" cy="27" r="4" fill="#fff"/><circle cx="35" cy="11" r="2.5" fill="#fff"/>
    </svg>
    <svg class="divider-icon" style="left:706px" viewBox="0 0 46 46" aria-hidden="true">
      <line x1="8" y1="38" x2="26" y2="20" stroke="#000" stroke-width="7" stroke-linecap="round"/>
      <circle cx="31" cy="15" r="10" fill="#000"/>
      <path d="M31 3 L40 12 L36 16 L27 7Z" fill="#fff"/>
    </svg>
    <span class="divider-line right"></span>
  </div>

  <ul class="service-list">
    <li>Internal Pivot Assessment &amp; Post Exploitation</li>
    <li>Advanced Product, Hardware &amp; RF Testing</li>
    <li>Mobile Application Assessment</li>
    <li>External Penetration Testing</li>
    <li>Internal Penetration Testing</li>
    <li>Web Application Penetration Testing</li>
  </ul>

  <footer class="site-footer">
    <h2 class="contact-title">Contact</h2>
    <ul class="contact-list">
      <li><svg viewBox="0 0 16 16" aria-hidden="true"><circle cx="8" cy="8" r="7" fill="none" stroke="#000" stroke-width="1.5"/><circle cx="8" cy="6.5" r="2.5"/><path d="M3.5 12.5a5 4 0 0 1 9 0"/></svg>Dale Corven</li>
      <li><svg viewBox="0 0 16 16" aria-hidden="true"><path d="M3 1.5l3 .5 1 3.5-2 1.5a9 9 0 0 0 4 4l1.5-2 3.5 1 .5 3-2 1.5C6 14 2 10 1.5 3.5z"/></svg>555.014.2290</li>
      <li><svg viewBox="0 0 16 16" aria-hidden="true"><rect x="1" y="3" width="14" height="10" rx="1"/><path d="M1.5 4l6.5 5 6.5-5" fill="none" stroke="#646464" stroke-width="1.3"/></svg>dale@tallharbor.example</li>
      <li><svg viewBox="0 0 16 16" aria-hidden="true"><circle cx="8" cy="8" r="7"/><path d="M5 4c2 1 1 3 3 3s1 3 3 4M10 3c-1 1 0 2 2 2" fill="none" stroke="#646464" stroke-width="1.3"/></svg>tallharbor.example</li>
    </ul>
    <p class="copyright">© Copyright 2017, by TallHarbor</p>
  </footer>
</body>
</html>
```